High end personal training flyer design

I want a flyer designed to be delivered to people's houses to interest them in high end (and, therefore, not cheap) personal training services.

Don't want standard pictures of people exercising, before and afters, etc. More something that will appeal to that more affluent market.

Flexible on size of flyer, but please make sure it is a standard size that I can get printed easily. Would like it not to look like a normal flyer you get through the letterbox, so if any particular sizes, shapes, etc are known to do that, then that would be a good start.

Text on flyer to be as follows:

Is this you:

Live in East Cheshire
Male, aged 30-50
A father
Cash rich, time poor
Find handling high pressure at work comfortable
But have a short fuse out of work – with the wife, kids, life in general, etc
Not happy with the way your body looks and feels
Know exactly what you should do to sort that, but struggling to actually do it for various reasons
Turned off by the standard menu of options for addressing that – gyms, slimming clubs, diets, etc

If so, you may be interested in what I do.

Some would call it Personal Training. Some would call it Coaching. I’m not interested in giving what I do labels.

What I am interested in is providing the best possible service (and results) for my clients – whatever that entails.

I work closely with one or two clients at a time to make sure they get exactly what they need.

If you would like to find out more about this, I usually meet for a coffee and a chat. To see if we both think our working together is a good idea.

No squeeze pages, no countdowns, mailing lists or false scarcity.

No plastering this flyer with ‘Before and afters’ – they are ten a penny and my clients don’t want to have pictures of them in their underwear spread around the local area.

Just give me a call and we’ll go from there.

My number is 07914562208.

Ray

Industry/Entity Type

Training

Requirements
Should not have
• Generic before and after or exercise type pictures

```html
<!DOCTYPE html>
<html lang="en">
<head>
<meta charset="utf-8">
<title>Personal Training Flyer</title>
<link rel="stylesheet" href="https://fonts.googleapis.com/css2?family=Advent+Pro:wght@300&family=Bebas+Neue&family=Open+Sans:wght@400;600&family=PT+Sans&display=swap">
<style>
  :root {
    --page-bg: #e9e7e4;
    --yellow: #ecd02a;
    --orange: #e8431f;
    --charcoal: #58585a;
    --white: #ffffff;
    --ink: #222222;
    --sky-top: #d4e8f6;
    --sky-bottom: #ffffff;
    --tag-grey: #a7a8aa;
    --tag-text: #ffffff;
    --photo-light: #d9d9d9;
    --photo-dark: #6a6a6a;
  }
  * { box-sizing: border-box; margin: 0; padding: 0; }
  html, body {
    width: 979px; height: 1200px; overflow: hidden;
    background: var(--page-bg);
  }
  .flyer {
    position: absolute; left: 101px; top: 50px;
    width: 777px; height: 1100px;
    background: var(--charcoal);
    overflow: hidden;
    box-shadow: 0 4px 14px rgba(0,0,0,.18);
  }
  .intro-panel {
    position: absolute; left: 0; top: 0; width: 379px; height: 500px;
    background: linear-gradient(180deg, var(--sky-top) 129px, var(--sky-bottom) 330px);
  }
  .headline-box {
    position: absolute; left: 0; top: 0; width: 379px; height: 129px;
    background: var(--yellow);
  }
  .headline {
    position: absolute; left: 22px; top: 20px;
    font-family: "Advent Pro", sans-serif; font-weight: 300;
    font-size: 76px; line-height: 1; color: var(--white);
  }
  .profile-list {
    position: absolute; left: 26px; top: 141px; width: 345px;
    list-style: none;
    font-family: "PT Sans", sans-serif; font-size: 15.5px; line-height: 24px;
    color: var(--ink);
  }
  .portrait {
    position: absolute; left: 379px; top: 0; width: 398px; height: 530px;
    background: radial-gradient(ellipse at 55% 45%, var(--photo-light) 0%, #a9a9a9 45%, var(--photo-dark) 100%);
  }
  .snapshot {
    position: absolute; background: var(--white); padding: 10px 10px 26px;
    box-shadow: 0 3px 8px rgba(0,0,0,.35);
  }
  .snapshot .fill { width: 100%; height: 100%; }
  .snapshot--weights { left: -28px; top: 470px; width: 230px; height: 232px; transform: rotate(-6deg); }
  .snapshot--weights .fill { background: linear-gradient(135deg, #cfc6bf, #8b7f77); }
  .snapshot--scale { left: 90px; top: 496px; width: 284px; height: 292px; transform: rotate(8deg); }
  .snapshot--scale .fill { background: linear-gradient(160deg, #b89a82, #6b5444 60%, #3a2e26); }
  .profile-hook {
    position: absolute; left: 22px; top: 433px;
    font-family: "PT Sans", sans-serif; font-size: 19px; line-height: 26px; color: var(--orange);
  }
  .label-banner {
    position: absolute; left: 345px; top: 516px; width: 432px; height: 138px;
  }
  .label-banner svg { position: absolute; inset: 0; }
  .label-lines {
    position: absolute; inset: 0; padding-top: 14px;
    text-align: center; color: var(--white);
    font-family: "Bebas Neue", sans-serif; font-size: 24px; line-height: 33px;
    letter-spacing: .3px;
  }
  .label-lines .rule { display: block; width: 370px; height: 2px; margin: 2px auto 4px; background: var(--yellow); }
  .body-copy {
    position: absolute; left: 384px; width: 374px;
    font-family: "Open Sans", sans-serif; font-size: 14.5px; line-height: 22px;
    color: var(--white); text-align: justify;
  }
  .body-copy p + p { margin-top: 22px; }
  .body-copy--service { top: 686px; }
  .body-copy--meet { top: 854px; }
  .divider { position: absolute; left: 374px; top: 833px; width: 386px; height: 2px; background: var(--yellow); }
  .no-nonsense-tag {
    position: absolute; left: 70px; top: 865px; width: 236px; height: 92px;
    transform: rotate(-15deg);
  }
  .no-nonsense-tag svg { position: absolute; inset: 0; }
  .no-nonsense-tag p {
    position: absolute; inset: 0; padding-top: 20px;
    text-align: center; color: var(--tag-text);
    font-family: "Open Sans", sans-serif; font-size: 12.5px; line-height: 16px; text-transform: uppercase;
  }
  .call-to-action {
    position: absolute; right: 17px; top: 976px;
    font-family: "Bebas Neue", sans-serif; font-size: 31px; line-height: 36px; color: var(--yellow);
    letter-spacing: .3px; white-space: nowrap;
  }
  .signature {
    position: absolute; right: 17px; top: 1026px;
    display: flex; align-items: center; gap: 10px; color: var(--yellow);
    font-family: "Advent Pro", sans-serif; font-weight: 300;
  }
  .signature .name { font-size: 52px; line-height: 1; margin-right: 4px; }
  .signature .phone { font-size: 36px; line-height: 1; }
</style>
</head>
<body>
  <main class="flyer">
    <section class="intro-panel"></section>
    <div class="headline-box"><h1 class="headline">Is this you?</h1></div>
    <ul class="profile-list">
      <li>Live in East Cheshire</li>
      <li>Male, aged 30-50</li>
      <li>A father</li>
      <li>Cash rich, time poor</li>
      <li>Find handling high pressure at work comfortable</li>
      <li>But have a short fuse out of work – with the wife, kids, life in general, etc</li>
      <li>Not happy with the way your body looks and feels</li>
      <li>Know exactly what you should do to sort that, but struggling to actually do it for various reasons</li>
      <li>Turned off by the standard menu of options for addressing that – gyms, slimming clubs, diets, etc</li>
    </ul>

    <div class="portrait" role="img" aria-label="Black and white photo of a puzzled man scratching his head"></div>

    <figure class="snapshot snapshot--weights"><div class="fill" role="img" aria-label="Snapshot of a hand holding a dumbbell"></div></figure>
    <figure class="snapshot snapshot--scale"><div class="fill" role="img" aria-label="Snapshot of bare feet on a bathroom scale"></div></figure>

    <p class="profile-hook">If so, you may be interested in what I do.</p>

    <div class="label-banner">
      <svg width="432" height="138" viewBox="0 0 432 138" aria-hidden="true">
        <path d="M6 10 L432 0 L432 130 L14 138 L0 118 L10 94 L2 70 L12 44 L3 24 Z" fill="var(--orange)"/>
      </svg>
      <div class="label-lines">
        Some would call it personal training.<br>
        Some would call it coaching.
        <span class="rule"></span>
        I’m not interested in giving what I do labels.
      </div>
    </div>

    <div class="body-copy body-copy--service">
      <p>What I am interested in is providing the best possible service (and results) for my clients – whatever that entails.</p>
      <p>I work closely with one or two clients at a time to make sure they get exactly what they need.</p>
    </div>
    <div class="divider"></div>
    <div class="body-copy body-copy--meet">
      <p>If you would like to find out more about this, I usually meet for a coffee and a chat. To see if we both think our working together is a good idea.</p>
    </div>

    <div class="no-nonsense-tag">
      <svg width="236" height="92" viewBox="0 0 236 92" aria-hidden="true">
        <path d="M4 4 L232 2 L226 20 L234 44 L228 68 L234 90 L6 88 L12 64 L2 42 L10 20 Z" fill="none" stroke="var(--tag-grey)" stroke-width="7"/>
      </svg>
      <p>No squeeze pages,<br>no countdowns,<br>mailing lists or false scarcity.</p>
    </div>

    <p class="call-to-action">Just give me a call and we’ll go from there.</p>
    <div class="signature">
      <span class="name">Ray</span>
      <svg width="34" height="34" viewBox="0 0 34 34" aria-hidden="true">
        <circle cx="17" cy="17" r="15" fill="none" stroke="var(--yellow)" stroke-width="2.5"/>
        <path d="M11 9 L14 9 L15.5 13 L13.5 14.5 C14.5 17 16.5 19 19 20 L20.5 18 L24.5 19.5 L24.5 22.5 C24.5 24 23 25 21.5 24.8 C15 24 10 19 9.2 12.5 C9 10.5 10 9 11 9 Z" fill="var(--yellow)"/>
      </svg>
      <span class="phone">07914562208</span>
    </div>
  </main>
</body>
</html>
```